Live Webcasting Host Wants Template/Theme to Jumpstare Ecommerce Site

Please,Please, Please READ ALL OF THE DESCRIPTION. Thank you.

I need a template for a look for my developer to work with in designing an ecommerce site where clients pay a monthly fee for streaming services and video on demand.

I'll need 2 pages designed:
1) public page
2) client log in landing page.

Please use a CMS (WP preferred) as this will allow is for further content to be added after delivery. Please include the pricing text in boxes in slides (pdf) to help fill out you design for the home page.

The attached slides are to give you a general layout of how I envision the pages. Yes I would like the Client page to be tabbed from the side like in the attached slide.

I've attached company logos for use along with the accompanying .psd and .ai files in the zip. Use the colors in logo in site design.

Thank you for your time.

Please, no designs. This is for a CMS for webpage design like WordPress or Joomla. Thanks. Added Friday, January 13, 2017

Target Market(s)

Churches, Organizations, Civic Organizations, Government Agencies (State, Local) -BUT don't let this deter your creativity. Decision makers/influencers will be video production and/or IT personnel.

Industry/Entity Type

It Company

Font styles to use
Sans Serif

Colors
f5f5f5
e8e8e8
333333
fece3e
cbcbcb
33a6d7
000000

Requirements
Must have
• Responsive Design
Nice to have
• One Page Design
Should not have
• SHOULD NOT HAVE White overall background but use white in other ways if you like.

```html
<!DOCTYPE html>
<html lang="en">
<head>
<meta charset="utf-8">
<title>Vantra – Login</title>
<link rel="stylesheet" href="https://fonts.googleapis.com/css2?family=Arimo:wght@400;700&family=Dosis:wght@400;500&family=Raleway:wght@500&display=swap">
<style>
  :root {
    --orange: #f7991f;
    --ink: #111111;
    --nav-text: #333333;
    --white: #ffffff;
    --placeholder: #a8a8a8;
    --social-blue: #4662a4;
    --rack-dark: #3a3d44;
    --rack-mid: #6f727a;
    --rack-light: #b9bcc2;
  }
  * { box-sizing: border-box; margin: 0; padding: 0; }
  html, body { width: 1200px; height: 845px; overflow: hidden; }
  body { position: relative; background: var(--rack-dark); font-family: "Arimo", Arial, sans-serif; }

  .site-header {
    position: absolute; left: 0; top: 0; width: 1200px; height: 100px;
    background: var(--white);
  }
  .brand {
    position: absolute; left: 59px; top: 28px;
    display: flex; align-items: center; gap: 12px;
  }
  .brand-mark { width: 28px; height: 28px; background: var(--orange); }
  .brand-name {
    font-family: "Arimo", Arial, sans-serif; font-weight: 700;
    font-size: 48px; line-height: 1; letter-spacing: 1px; color: var(--ink);
  }
  .header-login {
    position: absolute; left: 1063px; top: 10px; width: 77px; height: 31px;
    border: 2px solid var(--orange); color: var(--nav-text);
    font-size: 15px; letter-spacing: 0.5px;
    display: flex; align-items: center; justify-content: center;
  }
  .main-nav a {
    position: absolute; top: 64px; font-size: 15px; letter-spacing: 0.6px;
    color: var(--nav-text); text-decoration: none; white-space: nowrap;
  }
  .main-nav .is-active::after {
    content: ""; position: absolute; left: -3px; right: -3px; top: 31px;
    height: 4px; background: var(--orange);
  }

  .hero-photo {
    position: absolute; left: 0; top: 100px; width: 1200px; height: 745px;
    background:
      linear-gradient(90deg, var(--rack-light) 0%, var(--rack-dark) 8%, var(--rack-mid) 20%, var(--rack-dark) 32%, var(--rack-mid) 48%, var(--rack-dark) 60%, var(--rack-mid) 72%, var(--rack-light) 84%, var(--rack-dark) 94%, var(--rack-mid) 100%);
    opacity: 0.95;
  }

  .login-modal {
    position: absolute; left: 426px; top: 214px; width: 343px; height: 441px;
    background: var(--orange); border-radius: 3px;
    box-shadow: 0 0 14px rgba(0,0,0,0.35);
    text-align: center; color: var(--white);
  }
  .modal-close { position: absolute; right: 14px; top: 14px; width: 12px; height: 12px; }
  .modal-title {
    position: absolute; left: 0; right: 0; top: 30px;
    font-family: "Dosis", sans-serif; font-weight: 400; font-size: 48px;
    letter-spacing: 2px; line-height: 1;
  }
  .field {
    position: absolute; left: 47px; width: 255px; height: 34px;
    background: var(--white); border-radius: 6px;
    font-family: "Arimo", Arial, sans-serif; font-size: 15px; color: var(--placeholder);
    text-align: left; padding-left: 12px; line-height: 34px;
  }
  .field-username { top: 109px; }
  .field-password { top: 156px; }
  .submit-button {
    position: absolute; left: 138px; top: 209px; width: 74px; height: 32px;
    background: var(--ink); border-radius: 5px;
    font-family: "Raleway", sans-serif; font-weight: 500; font-size: 15px;
    line-height: 32px; color: var(--white);
  }
  .forgot-link {
    position: absolute; left: 0; right: 0; top: 265px;
    font-size: 16px; letter-spacing: 0.6px;
  }
  .divider {
    position: absolute; left: 59px; width: 233px; top: 309px;
    display: flex; align-items: center; gap: 10px; font-size: 14px;
  }
  .divider::before, .divider::after { content: ""; flex: 1; height: 1px; background: var(--white); }
  .social-button {
    position: absolute; left: 88px; top: 353px; width: 174px; height: 27px;
    background: var(--social-blue); border-radius: 2px;
    font-family: "Arimo", Arial, sans-serif; font-weight: 700; font-size: 11.5px;
    line-height: 27px; color: var(--white);
  }
  .register-link {
    position: absolute; left: 0; right: 0; top: 390px; font-size: 14px;
  }
</style>
</head>
<body>
  <header class="site-header">
    <div class="brand">
      <span class="brand-mark"></span>
      <span class="brand-name">vantra</span>
    </div>
    <div class="header-login">LOGIN</div>
    <nav class="main-nav">
      <a class="is-active" style="left:498px">FEATURES</a>
      <a style="left:632px">PRICING</a>
      <a style="left:749px">ABOUT US</a>
      <a style="left:881px">WEBCASTING 101</a>
      <a style="left:1068px">CONTACT</a>
    </nav>
  </header>

  <div class="hero-photo" role="img" aria-label="Blurred photo of server racks in a data centre"></div>

  <section class="login-modal">
    <svg class="modal-close" viewBox="0 0 12 12" aria-label="Close">
      <path d="M1 1 L11 11 M11 1 L1 11" stroke="#ffffff" stroke-width="3" stroke-linecap="round"/>
    </svg>
    <h1 class="modal-title">LOGIN</h1>
    <div class="field field-username">Username</div>
    <div class="field field-password">Password</div>
    <div class="submit-button">LOGIN</div>
    <div class="forgot-link">FORGOT PASSWORD?</div>
    <div class="divider">OR</div>
    <div class="social-button">Login with Friendnet</div>
    <div class="register-link">Click here to register</div>
  </section>
</body>
</html>
```